New Brochure Design for multiple brochures

We are looking for a designer to create a new template for our vireLUX family of modular and mobile biopharmaceutical facilities. We will be looking to put together a set of new brochures based on this design, likely using the original designer to complete the final layouts. The attached brochure is true to our current aesthetic and contains our basic corporate color scheme. However, we are open to changes to the colors and the overall look so long as they work with our logo. (FYI: Our president favors clean designs with abundant white space.) Overall, we are hoping to achieve a design that projects the high-tech nature of our company and equipment. This equipment is designed for and sold to biotech and pharmaceutical companies and the brochures should cater to that audience in their visual style.

Target Market(s)

Pharmaceutical Industry

Industry/Entity Type

Biotechnology

Font styles to use
Sans Serif

Requirements
Must have
• A layout design that provides a fresh look on the current brochures attached to this brief. The desired layout would have clean lines with a technology company feel. White space and a design that has a layout with sufficient spacing is important.
Nice to have
• Really like the idea of having a theme that emphasizes a product life cycle and conveys life science technology (gene therapy, cancer drug development) focus.
Should not have
• Cluttered objects and text. Must use the current logo format.

```html
<!DOCTYPE html>
<html lang="en">
<head>
<meta charset="utf-8">
<title>vireLUX Brochure – Inside Spread</title>
<link href="https://fonts.googleapis.com/css2?family=Montserrat:wght@400;500;600;700;800&display=swap" rel="stylesheet">
<style>
  :root {
    --canvas: #e3e3e3;
    --paper: #ffffff;
    --paper-mid: #eeeeee;
    --paper-right: #f6f6f6;
    --navy: #1f2f8c;
    --blue: #2d6fd6;
    --ink: #33363d;
    --muted: #80858f;
    --rule: #b9bcc2;
    --floor: #2f6fd0;
  }
  * { box-sizing: border-box; margin: 0; padding: 0; }
  html, body { width: 1200px; height: 768px; overflow: hidden; }
  body { background: var(--canvas); font-family: "Montserrat", Arial, sans-serif; color: var(--ink); position: relative; }

  .spread { position: absolute; left: 30px; top: 54px; width: 1140px; height: 660px; display: flex; box-shadow: 0 10px 30px rgba(0,0,0,.14); }
  .panel { position: relative; width: 380px; height: 660px; overflow: hidden; }
  .panel--intro { background: var(--paper); }
  .panel--modular { background: var(--paper-mid); border-left: 1px solid #d9d9d9; }
  .panel--mobile { background: var(--paper-right); border-left: 1px solid #d9d9d9; }

  /* Intro panel */
  .pillar { position: absolute; width: 160px; }
  .pillar__rule { position: absolute; height: 1px; background: var(--rule); }
  .pillar__title { font-size: 20px; font-weight: 700; color: var(--ink); line-height: 1.1; }
  .pillar__sub { margin-top: 6px; font-size: 8.5px; font-weight: 700; color: var(--ink); line-height: 1.3; }
  .pillar__sub em { font-style: normal; color: var(--blue); }
  .pillar__body { margin-top: 6px; font-size: 7px; line-height: 1.5; color: var(--muted); }
  .pillar__body b { color: var(--navy); }
  .pillar--faster { left: 28px; top: 130px; }
  .pillar--further { left: 200px; top: 44px; }
  .pillar--together { left: 200px; top: 196px; }

  .art { position: absolute; }
  .art--building { left: 0; top: 360px; width: 380px; height: 300px;
    background: linear-gradient(160deg, #f4f4f2 0%, #d9dadb 45%, #3a4f9a 70%, #6c9a4a 100%); }

  /* Product panels */
  .photo { position: absolute; }
  .brand { position: absolute; display: flex; align-items: center; gap: 6px;
    font-size: 18px; font-weight: 600; color: var(--navy); line-height: 1; }
  .brand__dot { width: 8px; height: 8px; background: var(--navy); }

  .section-title { position: absolute; left: 24px; right: 24px; text-align: center; font-size: 9px; font-weight: 700; color: var(--ink);
    border-bottom: 1px solid var(--rule); padding-bottom: 5px; }
  .bullets { position: absolute; display: flex; gap: 14px; }
  .bullets ul { width: 155px; list-style: none; }
  .bullets li { font-size: 6.8px; line-height: 1.45; color: var(--muted); padding-left: 8px; position: relative; margin-bottom: 4px; }
  .bullets li::before { content: ""; position: absolute; left: 0; top: 4px; width: 3px; height: 3px; border-radius: 50%; background: var(--muted); }

  .zone-label { position: absolute; font-size: 6.5px; line-height: 1.3; color: var(--muted); text-align: center; }
  .zone-label b { display: block; color: var(--ink); font-weight: 700; }
  .leaders { position: absolute; left: 0; top: 0; }
</style>
</head>
<body>
<main class="spread">

  <!-- Panel 1: value pillars -->
  <section class="panel panel--intro">
    <div class="pillar__rule" style="left:28px; top:118px; width:140px;"></div>
    <div class="pillar__rule" style="left:200px; top:30px; width:150px;"></div>

    <article class="pillar pillar--faster">
      <h2 class="pillar__title">Go Faster</h2>
      <p class="pillar__sub">Accelerate your time to market with a <em>manufactured solution</em></p>
      <p class="pillar__body"><b>vireLUX</b> units are built off-site in parallel with site work, so clean space arrives tested, qualified and ready for process transfer in weeks rather than years.</p>
    </article>

    <article class="pillar pillar--further">
      <h2 class="pillar__title">Go Further</h2>
      <p class="pillar__sub">Optimized for a wide array of <em>bioprocess applications</em></p>
      <p class="pillar__body">Self-contained cleanroom pods support cell therapy, gene therapy, vaccines and biologics, with each layout tailored to the process and scaled to the site.</p>
    </article>

    <article class="pillar pillar--together">
      <h2 class="pillar__title">Go Together</h2>
      <p class="pillar__sub">Adjustable as your capacity <em>requirements change</em></p>
      <p class="pillar__body">Our team partners with engineering and quality groups from concept to qualification, and units can be added, moved or reconfigured as demand grows.</p>
    </article>

    <div class="art art--building" role="img" aria-label="Cutaway rendering of a building housing several white modular cleanroom pods, with trees around it"></div>
  </section>

  <!-- Panel 2: modular platform -->
  <section class="panel panel--modular">
    <div class="brand" style="left:24px; top:24px;"><span class="brand__dot"></span>vireLUX</div>
    <div class="photo" style="left:0; top:70px; width:220px; height:150px; background:linear-gradient(135deg,#2b2d31,#6d7077 55%,#d8d9db);" role="img" aria-label="Photo of a white modular cleanroom unit in a dark studio"></div>
    <div class="photo" style="left:160px; top:20px; width:220px; height:120px; background:linear-gradient(180deg,#f7f7f7,#d4d6d9);" role="img" aria-label="Photo of a bright white cleanroom interior"></div>

    <h3 class="section-title" style="top:240px;">Modular Bioproduction and R&amp;D Platforms</h3>
    <div class="bullets" style="left:26px; top:266px;">
      <ul>
        <li>Advanced infrastructure and capabilities in a factory-built, fully tested unit</li>
        <li>Permanent installation that meets the strictest regulatory codes for current applications</li>
      </ul>
      <ul>
        <li>Proprietary technology protects and isolates multiple modules</li>
        <li>Self-contained for use in existing buildings</li>
        <li>Available for lease or purchase</li>
      </ul>
    </div>

    <div class="art" style="left:24px; top:360px; width:332px; height:130px; background:linear-gradient(180deg,#d9dadc 0%,#c4c6c9 40%,var(--floor) 75%,#1f4fa6 100%);" role="img" aria-label="Cutaway illustration of a modular cleanroom floor plan with blue floors and process equipment"></div>

    <svg class="leaders" width="380" height="660" aria-hidden="true">
      <g stroke="#555" stroke-width=".6" fill="none">
        <line x1="50" y1="480" x2="50" y2="540"/>
        <line x1="120" y1="470" x2="120" y2="540"/>
        <line x1="200" y1="470" x2="200" y2="540"/>
        <line x1="280" y1="460" x2="280" y2="540"/>
        <line x1="340" y1="440" x2="340" y2="520"/>
      </g>
    </svg>
    <div class="zone-label" style="left:26px; top:544px; width:50px;">Entry Room<b>CNC</b></div>
    <div class="zone-label" style="left:86px; top:544px; width:70px;">Entry Antechamber / Gowning<b>ISO 8 (Grade D)</b></div>
    <div class="zone-label" style="left:164px; top:544px; width:74px;">Exit Antechamber / Degowning<b>ISO 8 (Grade D)</b></div>
    <div class="zone-label" style="left:246px; top:544px; width:70px;">Production Suite<b>ISO 7 (Grade C)</b></div>
    <div class="zone-label" style="left:318px; top:524px; width:48px;">Material Airlock<b>ISO 8 (Grade D)</b></div>
  </section>

  <!-- Panel 3: mobile platform -->
  <section class="panel panel--mobile">
    <div class="photo" style="left:200px; top:14px; width:160px; height:90px; background:linear-gradient(135deg,#3a3d44,#9aa0a8 50%,#e4e6e8);" role="img" aria-label="Photo of bioprocess equipment inside a cleanroom"></div>
    <div class="photo" style="left:150px; top:70px; width:90px; height:90px; background:linear-gradient(180deg,#8b8e94,#dfe1e3);" role="img" aria-label="Photo of a stainless steel bioreactor"></div>

    <div class="brand" style="left:26px; top:154px;"><span class="brand__dot"></span>vireLUX</div>

    <div class="photo" style="left:40px; top:190px; width:300px; height:130px; background:linear-gradient(180deg,#3b3f5c 0%,#c77a4a 45%,#f2f2f4 60%,#d5d6da 100%);" role="img" aria-label="Photo of a white mobile cleanroom trailer parked at sunset"></div>

    <h3 class="section-title" style="top:340px;">Mobile Bioproduction and R&amp;D Platforms</h3>
    <div class="bullets" style="left:26px; top:366px;">
      <ul>
        <li>Rapid deployment of mobile clean rooms and easily relocated production suites</li>
        <li>Quickly operational upon delivery and easily activated</li>
        <li>Optimal for providing advanced capacities globally, including remote locations</li>
      </ul>
      <ul>
        <li>Ideal for short-term projects, surge capacity and interim needs during construction</li>
        <li>Multiple configurations provide flexibility and availability for your process. Available for lease or purchase</li>
      </ul>
    </div>

    <div class="art" style="left:24px; top:460px; width:332px; height:90px; background:linear-gradient(180deg,#e8e9eb 0%,#c9cbce 40%,var(--floor) 80%,#1f4fa6 100%); border-radius:4px 20px 20px 4px;" role="img" aria-label="Cutaway illustration of a mobile cleanroom trailer interior with blue floors and equipment"></div>

    <svg class="leaders" width="380" height="660" aria-hidden="true">
      <g stroke="#555" stroke-width=".6" fill="none">
        <line x1="110" y1="540" x2="110" y2="590"/>
        <line x1="220" y1="530" x2="220" y2="590"/>
        <line x1="320" y1="520" x2="320" y2="580"/>
      </g>
    </svg>
    <div class="zone-label" style="left:76px; top:594px; width:70px;">Production Suite<b>ISO 7 (Grade C)</b></div>
    <div class="zone-label" style="left:182px; top:594px; width:76px;">Antechamber / Gowning<b>ISO 8 (Grade D)</b></div>
    <div class="zone-label" style="left:296px; top:584px; width:50px;">Admin Area<b>CNC</b></div>
  </section>

</main>
</body>
</html>
```